PLUMA Project Roll Up Banner 85x200 cm (1:10, 1200 dpi)

PLUMA is a EU-funded project to promote female entrepreneurship networks. The project is developed by 9 partners from 7 different countries.
The banner is to be used throughout the project in exhibitions, conferences, roundtables, etc.
It has to include the following graphic elements, which cannot be modified beyond scaling:
- PLUMA logo
- EU logo (cannot be modified in any way, and cannot have any kind of background, but pure white).
- 9 partners logos
- (plain square) link (with logo)
- (plain square) link (with logo)
- Project's website (www.pluma-circle.example)
The text to be included:
Promoting Lasting Uplift through Mentoring and Alliances
PLUMA: Contributes to the strengthening of the links between women entrepreneurs and the mainstream of new technologies, educational, and training practices offered all over Europe.
GOOD PRACTICES: Compilation of EU projects promoting female entrepreneurship and ICT systems for learning, supporting, and training women entrepreneurs.
NETWORK: Strengthening of linkages between EU women entrepreneurs, project managers, learning communities, multipliers, and society to encourage a knowledge-sharing environment through the creation of the PLUMA circle.
ONE-STOP SHOP: Development of a multi-lingual EU online platform, where valuable an innovative EU learning opportunities can be found and accessed at one single place, as well as fostering new business opportunities by a Virtual Market.
The banner has to be attractive the modern female entrepreneur. It has to be easy to read, and present a fresh and exciting identity.
The banner has to include 5 additional centimetres on the top, and 10 on the bottom.
The last partner logo has been uploaded now.
Female entrepreneurs
Higher Educational Institutions
Government Female Representatives
Environment

```html
<!DOCTYPE html>
<html lang="en">
<head>
<meta charset="utf-8">
<title>PLUMA Project Roll Up Banner</title>
<link rel="stylesheet" href="https://fonts.googleapis.com/css2?family=Advent+Pro:wght@400;500&family=Arimo:wght@400;700&display=swap">
<style>
  :root {
    --teal: #3fdfc6;
    --navy: #25237f;
    --navy-deep: #1c1a6e;
    --sky-blue: #4aa6e8;
    --white: #ffffff;
    --ink: #333333;
    --rule: #b8b8b8;
    --photo-light: #d9dde2;
    --photo-mid: #8c959f;
    --photo-dark: #3c4650;
  }
  * { margin: 0; padding: 0; box-sizing: border-box; }
  html, body { width: 1200px; height: 3033px; overflow: hidden; background: var(--white); }
  .banner { position: relative; width: 1200px; height: 3033px; overflow: hidden; background: var(--white); font-family: "Arimo", Arial, sans-serif; }

  .band-top { position: absolute; left: 0; top: 0; width: 1200px; height: 71px; background: var(--teal); }

  .hero-photo {
    position: absolute; left: 0; top: 71px; width: 1200px; height: 1284px;
    background:
      radial-gradient(ellipse 260px 520px at 640px 780px, #5a5e66 0%, rgba(90,94,102,0) 100%),
      linear-gradient(90deg, var(--photo-light) 0%, #b9c0c8 20%, var(--photo-mid) 45%, #a7b0ba 70%, var(--photo-dark) 100%);
  }

  .brand-band { position: absolute; left: 0; top: 1190px; width: 1200px; height: 305px; background: var(--white); }
  .brand-fade {
    position: absolute; left: 430px; top: 1355px; width: 770px; height: 140px;
    background: linear-gradient(90deg, rgba(37,35,127,0) 0%, rgba(37,35,127,0.35) 45%, var(--navy) 100%);
  }
  .brand-logo { position: absolute; left: 92px; top: 1330px; display: flex; align-items: center; gap: 22px; }
  .brand-logo .mark { width: 44px; height: 44px; border-radius: 50%; background: var(--navy); }
  .brand-logo .name { font-family: "Advent Pro", sans-serif; font-weight: 400; font-size: 86px; line-height: 1; color: var(--navy); letter-spacing: 2px; }
  .brand-tagline { position: absolute; left: 92px; top: 1440px; font-family: "Advent Pro", sans-serif; font-size: 27px; color: var(--sky-blue); letter-spacing: 0.5px; }

  .info-panel { position: absolute; left: 0; top: 1495px; width: 1200px; height: 1062px; background: var(--navy); color: var(--white); }
  .headline { position: absolute; left: 0; top: 45px; width: 1200px; text-align: center; font-family: "Advent Pro", sans-serif; font-weight: 400; font-size: 62px; line-height: 70px; }

  .pillar { position: absolute; left: 45px; width: 1130px; display: flex; align-items: center; }
  .pillar-label { width: 266px; font-family: "Advent Pro", sans-serif; font-size: 44px; line-height: 44px; text-transform: uppercase; }
  .pillar-text { width: 864px; font-size: 27.5px; line-height: 36px; }
  .pillar-core { top: 303px; }
  .pillar-practices { top: 490px; }
  .pillar-network { top: 648px; }
  .pillar-shop { top: 843px; }

  .partners { position: absolute; left: 0; top: 2557px; width: 1200px; height: 198px; background: var(--white); }
  .partner-row { position: absolute; left: 25px; width: 1150px; height: 70px; display: flex; align-items: center; justify-content: space-between; }
  .partner-row.first { top: 25px; }
  .partner-row.second { top: 105px; }
  .partner { display: flex; align-items: center; gap: 10px; font-family: "Arimo", sans-serif; font-size: 25px; color: var(--ink); white-space: nowrap; }
  .partner .dot { width: 22px; height: 22px; background: var(--navy); }
  .partner-divider { width: 2px; height: 62px; background: var(--rule); }
  .partner-badge { width: 150px; height: 60px; background: var(--navy); }

  .rule-teal { position: absolute; left: 0; top: 2755px; width: 1200px; height: 12px; background: var(--teal); }

  .footer-links { position: absolute; left: 0; top: 2767px; width: 1200px; height: 119px; display: flex; align-items: center; justify-content: space-between; padding: 0 45px; font-size: 29px; color: var(--ink); }
  .footer-link { display: flex; align-items: center; gap: 16px; }
  .footer-link .icon-square { width: 30px; height: 30px; background: var(--navy); }
  .footer-link svg { width: 36px; height: 36px; }

  .band-bottom { position: absolute; left: 0; top: 2886px; width: 1200px; height: 147px; background: var(--teal); }
</style>
</head>
<body>
<div class="banner">
  <div class="band-top"></div>

  <div class="hero-photo" role="img" aria-label="Photo of a smiling young woman entrepreneur in a grey cardigan and white scarf standing among modern glass office buildings"></div>

  <div class="brand-band"></div>
  <div class="brand-fade"></div>
  <div class="brand-logo"><span class="mark"></span><span class="name">PLUMA</span></div>
  <div class="brand-tagline">Women - Entrepreneurship - Networking</div>

  <section class="info-panel">
    <h1 class="headline">Promoting Lasting Uplift<br>through Mentoring<br>and Alliances</h1>

    <div class="pillar pillar-core">
      <div class="pillar-label">PLUMA</div>
      <p class="pillar-text">Contributes to the strengthening of the links between women entrepreneurs and the mainstream of new technologies, educational, and training practices offered all over Europe.</p>
    </div>
    <div class="pillar pillar-practices">
      <div class="pillar-label">Good<br>Practices</div>
      <p class="pillar-text">Compilation of EU projects promoting female entrepreneurship and ICT systems for learning, supporting, and training women entrepreneurs.</p>
    </div>
    <div class="pillar pillar-network">
      <div class="pillar-label">Network</div>
      <p class="pillar-text">Strengthening of linkages between EU women entrepreneurs, project managers, learning communities, multipliers, and society to encourage a knowledge-sharing environment through the creation of the PLUMA circle.</p>
    </div>
    <div class="pillar pillar-shop">
      <div class="pillar-label">One-Stop<br>Shop</div>
      <p class="pillar-text">Development of a multi-lingual EU online platform, where valuable an innovative EU learning opportunities can be found and accessed at one single place, as well as fostering new business opportunities by a Virtual Market.</p>
    </div>
  </section>

  <section class="partners" aria-label="Project partners">
    <div class="partner-row first">
      <div class="partner"><span class="dot"></span>Orbita Lab</div>
      <div class="partner-divider"></div>
      <div class="partner">Halden College</div>
      <div class="partner-divider"></div>
      <div class="partner">nexohub.example</div>
      <div class="partner-divider"></div>
      <div class="partner">Norvik University</div>
      <div class="partner-divider"></div>
      <div class="partner">Ceda Advisory</div>
    </div>
    <div class="partner-row second">
      <div class="partner">Prodana</div>
      <div class="partner-divider"></div>
      <div class="partner">Steinhof University</div>
      <div class="partner-divider"></div>
      <div class="partner">lumeo</div>
      <div class="partner-divider"></div>
      <div class="partner">trevia consultancy</div>
      <div class="partner-divider"></div>
      <div class="partner-badge" role="img" aria-label="Funding programme badge"></div>
    </div>
  </section>

  <div class="rule-teal"></div>

  <footer class="footer-links">
    <div class="footer-link"><span class="icon-square"></span>/llp.pluma</div>
    <div class="footer-link">
      <svg viewBox="0 0 36 36" aria-hidden="true"><circle cx="18" cy="18" r="15" fill="none" stroke="#25237f" stroke-width="2.5"/><ellipse cx="18" cy="18" rx="6.5" ry="15" fill="none" stroke="#25237f" stroke-width="2"/><line x1="3" y1="18" x2="33" y2="18" stroke="#25237f" stroke-width="2"/></svg>
      www.pluma-circle.example
    </div>
    <div class="footer-link"><span class="icon-square"></span>/groups/PLUMA-circle-4402718</div>
  </footer>

  <div class="band-bottom"></div>
</div>
</body>
</html>
```